Wedding / 60th Birthday Invitations

We need invitation design for our Wedding and Partners 60th Birthday.
We have come up with a design that reflects both ourselves and the events but needs fine tuning and we are hoping you can do this for us.
We want bridal owls sitting in a Velmora car holding a 60th balloon.
Please see sketches attached with invite details. Colour theme is Black, Red & White.
We also require a print for the poem for Wishing Well & Acceptance Cards
Thank you

```html
<!DOCTYPE html>
<html lang="en">
<head>
<meta charset="utf-8">
<title>Wedding and 60th Birthday Invitation</title>
<link rel="stylesheet" href="https://fonts.googleapis.com/css2?family=Dancing+Script:wght@400;500&display=swap">
<style>
  :root {
    --paper: #bdbdbd;
    --road: #5b5b5b;
    --road-edge: #111111;
    --ink: #111111;
    --light: #ffffff;
    --car-red: #d8262b;
    --car-deep: #a8171c;
    --balloon-tone: #d94a5a;
  }
  html, body {
    margin: 0;
    padding: 0;
    overflow: hidden;
    background: var(--paper);
  }
  .invitation {
    position: relative;
    width: 1200px;
    height: 858px;
    background: var(--paper);
    overflow: hidden;
    font-family: "Dancing Script", cursive;
    color: var(--ink);
  }
  .scenery {
    position: absolute;
    inset: 0;
  }
  .line {
    position: absolute;
    margin: 0;
    white-space: nowrap;
    line-height: 1;
  }
  .names {
    left: 84px;
    top: 66px;
    font-size: 42px;
  }
  .centered {
    left: 0;
    width: 710px;
    text-align: center;
    font-size: 40px;
  }
  .invite { top: 116px; }
  .marriage { top: 170px; }
  .and-line { top: 224px; }
  .birthday { top: 270px; }
  .light { color: var(--light); }
  .dark { color: var(--ink); }
  .details {
    position: absolute;
    left: 134px;
    top: 350px;
    font-size: 32px;
    line-height: 48px;
    margin: 0;
  }
  .details dt {
    float: left;
    clear: left;
    width: 96px;
    color: var(--light);
  }
  .details dd {
    margin: 0 0 0 96px;
    color: var(--ink);
  }
  .car-maker {
    position: absolute;
    left: 566px;
    top: 660px;
    font-size: 22px;
    color: var(--light);
    line-height: 1;
  }
</style>
</head>
<body>
<main class="invitation">
  <svg class="scenery" width="1200" height="858" viewBox="0 0 1200 858">
    <defs>
      <linearGradient id="car-fill" x1="0" y1="0" x2="0" y2="1">
        <stop offset="0" stop-color="var(--car-red)"/>
        <stop offset="1" stop-color="var(--car-deep)"/>
      </linearGradient>
    </defs>
    <polygon class="road" points="0,738 1200,515 1200,858 0,858" fill="var(--road)"/>
    <line class="road-edge" x1="0" y1="738" x2="1200" y2="515" stroke="var(--road-edge)" stroke-width="12"/>
    <rect class="balloon-area" x="966" y="162" width="182" height="196" rx="10" fill="var(--balloon-tone)" role="img" aria-label="Colourful party balloon showing the number 60, held on a red string"/>
    <rect class="car-with-owls" x="518" y="560" width="630" height="252" rx="24" fill="url(#car-fill)" role="img" aria-label="Red convertible car carrying a bride owl in a veil and a groom owl in a top hat"/>
  </svg>

  <span class="car-maker">Velmora</span>

  <p class="line names"><span class="light">Lena Hartley</span> <span class="dark">and</span> <span class="light">Owen Callister</span></p>
  <p class="line centered invite dark">Invite you to celebrate our</p>
  <p class="line centered marriage light">Marriage</p>
  <p class="line centered and-line dark">and</p>
  <p class="line centered birthday light">Owen’s 60th Birthday</p>

  <dl class="details">
    <dt>Date:</dt><dd>Saturday October 8th, 2016</dd>
    <dt>Time:</dt><dd>5 PM</dd>
    <dt>Venue:</dt><dd>The Copper Kettle Brewery</dd>
    <dd>418 Marlow Rd</dd>
    <dd>Marlow Valley WA</dd>
  </dl>
</main>
</body>
</html>
```